Flyer-Design für Kanutouristiker (Kanu Vermietung) Folgeaufträge!!
Zielgruppe
Wir veranstalten Kanu - und Erlebnistouren. Vermieten Kanus, Schlauchboote (Rafts), SUP (Stand up Paddling) und Fahrräder.
Für Gruppen, Betriebe, Schulklassen, Vereine, Familien, Junggesellenabschiede, Geburtstage usw.
Aufgabenstellung
Wir möchten einen ansprechenden Flyer erstellen lassen, der Lust auf unsere Angebote machen soll.
Hier handelt es sich um einen DIN lang (A4) Wickelfalz Falter (6 Seiter)
Mit unseren Angeboten. Beispielbilder sind im Anhang mithochgeladen. Es können weitere geliefert werden- oder Sie sehen sich einmal auf unserer Webseite um.
Wenig Text- lassen Sie die Bilder sprechen!!
Der Flyer soll lust auf eine Tour bei uns machen!
Der Flyer soll natürlich wirken.
Unsere CI wird schon durch unser Logo mitgegeben- es müssen nicht unbeding gr. Flächen mit unseren Farben gefüllt werden!!
Uns sprechen filigrane, künstlerische Designs an. Aber bitte die natürlichkeit nicht aus den Augen verlieren. Wir sind OUTDOORveranstalter- unsere Aktionen finden in der Natur statt!
Eine Variante, die ich aus zahlreichen Designs erarbeitet habe:
Nutzen Sie ein grosses Bild als Header (Kopfzeile) das auch z.B. im Orangeton (Logofarbe) überzeichnet - oder auch nur weiss (milchig) verändert sein darf.
Hierauf einen geeigneten Sinnspruch (Überschrift) z.B. "..mehr als nur ein Abenteuer"
der passend sein muss.
Etwas Poetisches vielleicht.... kurz und prägnant. (Natur, ökologie, Wasser, reisen...).
Bilder groß und darauf überlagert kleinere eingefasst in Rahmen.
Zum Textinhalt
Titelseite:
was machen wir?
Paddel- & Radtouren im Weser-Leinebergland, tolles Bild und unser Logo
evtl. noch für wen geeignet?
Schulklassen, Betriebe, Vereine, Familien, Junggesellenabschiede etc.
Innenseite(n):
Bilder, Bilder, Bilder (vielleicht gr. Hintergrundbild, dann kleine Bilder drauf mit passender Überschrift: z.B. Abenteuer im Tivorunde, Stand up paddling, Teambuilding Flossbau, Radverleih, Strudel & Speiche, usw.
Rückseite:
Unsere Kontaktdaten
Firmenname
Webseite
Mailadresse
Hausanschrift
plaudernetz
QR Code
LOGO
Toll wäre ein..

```html
<!DOCTYPE html>
<html lang="de">
<head>
<meta charset="utf-8">
<title>Flusszeit Kanutouristik – Faltflyer</title>
<link rel="stylesheet" href="https://fonts.googleapis.com/css2?family=Kaushan+Script&family=Raleway:wght@300;400&family=Open+Sans:wght@400;700&display=swap">
<style>
  :root {
    --red: #c0151f;
    --orange: #f09000;
    --white: #ffffff;
    --stage: #444444;
    --ink: #333333;
  }
  * { margin: 0; padding: 0; box-sizing: border-box; }
  html, body { width: 980px; height: 1200px; overflow: hidden; background: var(--stage); }
  .canvas { position: relative; width: 980px; height: 1200px; }
  .panel { position: absolute; width: 251px; height: 528px; overflow: hidden; background: var(--white); }
  .panel svg.bg { position: absolute; inset: 0; width: 251px; height: 528px; }
  .row-outer .panel { top: 59px; }
  .row-inner .panel { top: 613px; }
  .col-1 { left: 104px; } .col-2 { left: 364px; } .col-3 { left: 624px; }

  .title { position: absolute; font-family: "Kaushan Script", cursive; line-height: 1; white-space: nowrap; }
  .title--orange { color: var(--orange); }
  .title--red { color: var(--red); }
  .subtitle { position: absolute; font-family: "Kaushan Script", cursive; font-size: 12px; line-height: 1; letter-spacing: -0.3px; white-space: nowrap; }
  .body-copy { position: absolute; font-family: "Raleway", sans-serif; font-weight: 300; font-size: 10.2px; line-height: 12.9px; color: var(--ink); }
  .body-copy p + p { margin-top: 2px; }

  .brand-name { position: absolute; font-family: "Open Sans", sans-serif; font-weight: 700; display: flex; align-items: center; gap: 5px; }
  .brand-name .dot { width: 12px; height: 12px; border-radius: 50%; }

  .contact { position: absolute; left: 0; width: 251px; top: 255px; text-align: center; color: var(--white); font-family: "Open Sans", sans-serif; font-size: 7px; line-height: 9.5px; }
  .contact .company { font-weight: 700; letter-spacing: 0.6px; margin-bottom: 6px; font-size: 7.2px; }
  .contact .block + .block { margin-top: 5px; }

  .cover-claim { position: absolute; left: 81px; top: 425px; font-family: "Open Sans", sans-serif; font-weight: 700; line-height: 1; letter-spacing: 1px; }
  .cover-claim span { display: block; }
  .cover-claim .small { font-size: 26px; color: var(--orange); }
  .cover-claim .big { font-size: 34px; color: var(--red); margin: 1px 0; }
</style>
</head>
<body>
<div class="canvas">

  <div class="row-outer">

    <section class="panel col-1 panel--sup-bike">
      <svg class="bg" viewBox="0 0 251 528">
        <defs>
          <linearGradient id="g-sup" x1="0" y1="0" x2="0" y2="1">
            <stop offset="0" stop-color="#5d7a3a"/><stop offset="0.45" stop-color="#6b7e86"/><stop offset="1" stop-color="#7fbf5a"/>
          </linearGradient>
          <linearGradient id="g-meadow" x1="0" y1="0" x2="0" y2="1">
            <stop offset="0" stop-color="#8fb0c8"/><stop offset="0.4" stop-color="#5f8f3a"/><stop offset="1" stop-color="#7fae45"/>
          </linearGradient>
          <linearGradient id="g-bike" x1="0" y1="0" x2="1" y2="1">
            <stop offset="0" stop-color="var(--orange)"/><stop offset="1" stop-color="var(--red)"/>
          </linearGradient>
        </defs>
        <circle cx="163" cy="42" r="67" fill="url(#g-sup)" stroke="var(--red)" stroke-width="5" role="img" aria-label="Foto: Stand-up-Paddler auf dem Fluss, Bugspitze eines grünen Boards"/>
        <circle cx="48" cy="125" r="51" fill="url(#g-meadow)" stroke="var(--orange)" stroke-width="5" role="img" aria-label="Foto: Gruppe mit roten Booten auf einer Wiese"/>
        <path d="M190,395 C215,420 250,440 251,470 V528 H120 C150,500 190,470 190,395 Z" fill="url(#g-bike)" opacity="0.85" role="img" aria-label="Illustration: Radfahrer"/>
      </svg>
      <h2 class="title title--orange" style="right:25px; top:118px; font-size:26px; text-align:right; line-height:32px;">Stand up<br>Paddeling</h2>
      <div class="subtitle" style="right:25px; top:184px; color:var(--red);">Paddeln im Stehen.</div>
      <div class="body-copy" style="left:25px; top:203px; width:202px;">
        <p>Egal ob Sie lieber ruhig paddeln möchten - zum Entspannen, sich einer Fitnesseinheit unterziehen möchten, oder es lieber in etwas bewegterem Wasser mögen- beim Stehpaddeln ist jeder richtig!</p>
      </div>
      <h2 class="title title--orange" style="left:25px; top:291px; font-size:26px;">Radtouren</h2>
      <div class="subtitle" style="left:25px; top:324px; color:var(--red);">Paddeln im Stehen.</div>
      <div class="body-copy" style="left:25px; top:345px; width:155px;">
        <p>Bei uns bekommen Sie hoch-wertige Mietfahrräder für Ihren Urlaub oder Ihre kleine Tour im Weser-Leinebergland.</p>
        <p>Ein leichter Alurahmen, gefederte Sattelstütze und eine 7- Gang Nabenschaltung zeichnen unsere Räder aus.</p>
      </div>
    </section>

    <section class="panel col-2 panel--contact" style="background:var(--red);">
      <svg class="bg" viewBox="0 0 251 528">
        <path d="M0,0 H251 V121 C180,115 70,100 54,75 C45,55 100,45 127,33 C100,15 40,15 0,17 Z" fill="var(--white)" stroke="var(--orange)" stroke-width="20"/>
        <path d="M0,0 H251 V121 C180,115 70,100 54,75 C45,55 100,45 127,33 C100,15 40,15 0,17 Z" fill="var(--white)"/>
      </svg>
      <div class="brand-name" style="left:0; width:251px; justify-content:center; top:202px; color:var(--white); font-size:12px;">
        <span class="dot" style="background:var(--white);"></span>flusszeit-erleben.de
      </div>
      <div class="contact">
        <div class="company">FLUSSZEIT<br>KANUTOURISTIK</div>
        <div class="block">Hanne Vollmer<br>37000 Lindhagen (Auenfeld/Weser)</div>
        <div class="block">Tel.:&nbsp;&nbsp; 0 55 00 - 12 34 56<br>Mobil: 0 15 00 - 98 76 543</div>
      </div>
    </section>

    <section class="panel col-3 panel--cover">
      <svg class="bg" viewBox="0 0 251 528">
        <defs>
          <linearGradient id="g-raft" x1="0" y1="0" x2="0" y2="1">
            <stop offset="0" stop-color="#6f9a3e"/><stop offset="0.25" stop-color="#b9b3a2"/><stop offset="0.45" stop-color="#c9594a"/><stop offset="0.75" stop-color="#2a2a33"/><stop offset="1" stop-color="#3a2a2a"/>
          </linearGradient>
        </defs>
        <rect x="0" y="120" width="251" height="408" fill="url(#g-raft)" role="img" aria-label="Foto: jubelnde Gruppe mit Paddeln in einem roten Schlauchboot"/>
        <path d="M0,117 C80,118 170,120 251,124 V153 C170,145 80,140 0,137 Z" fill="var(--orange)"/>
        <path d="M0,0 H251 V124 C170,120 80,118 0,117 Z" fill="var(--white)"/>
      </svg>
      <div class="brand-name" style="left:0; width:251px; justify-content:center; top:52px; color:var(--orange); font-size:16px;">
        <span class="dot" style="background:var(--red);"></span>flusszeit-erleben.de
      </div>
      <h1 class="cover-claim">
        <span class="small">AUF DEM</span>
        <span class="big">WASSER</span>
        <span class="small">ZU HAUSE.</span>
      </h1>
    </section>
  </div>

  <div class="row-inner">

    <section class="panel col-1 panel--canoe">
      <svg class="bg" viewBox="0 0 251 528">
        <defs>
          <linearGradient id="g-canoe" x1="0" y1="0" x2="0" y2="1">
            <stop offset="0" stop-color="#5e8f34"/><stop offset="0.55" stop-color="#4f7a2c"/><stop offset="0.8" stop-color="#c33a32"/><stop offset="1" stop-color="#6f7f5a"/>
          </linearGradient>
        </defs>
        <rect x="0" y="190" width="251" height="338" fill="url(#g-canoe)" role="img" aria-label="Foto: Gruppe paddelt im roten Kanadier auf dem Fluss"/>
        <path d="M0,0 H251 V358 C150,340 65,295 75,262 C90,230 182,222 181,205 C180,190 60,186 0,192 Z" fill="var(--white)" stroke="var(--orange)" stroke-width="20"/>
        <path d="M0,0 H251 V358 C150,340 65,295 75,262 C90,230 182,222 181,205 C180,190 60,186 0,192 Z" fill="var(--white)"/>
      </svg>
      <h2 class="title title--red" style="left:25px; top:24px; font-size:26px;">Kanutouren</h2>
      <div class="subtitle" style="left:25px; top:57px; color:var(--orange); font-size:11px;">Natur pur im Weser- und Leinebergland</div>
      <div class="body-copy" style="left:27px; top:80px; width:205px;">
        <p>Genießen Sie die Orte aus einer anderen Perspektive. Erkunden Sie die Landschaft, erleben Sie wunderbare Flüsse und genießen Sie ein einmaliges Erlebnis. Die große Weser, die wilde Emmer oder die kleine Nethe - jeder Fluss garantiert einen hohen Funfactor.</p>
      </div>
    </section>

    <section class="panel col-2 panel--raft">
      <svg class="bg" viewBox="0 0 251 528">
        <defs>
          <linearGradient id="g-tipi" x1="0" y1="0" x2="0" y2="1">
            <stop offset="0" stop-color="#e6dcc0"/><stop offset="1" stop-color="#7a8f5a"/>
          </linearGradient>
          <linearGradient id="g-canoe2" x1="0" y1="0" x2="0" y2="1">
            <stop offset="0" stop-color="#4f7a2c"/><stop offset="0.6" stop-color="#c33a32"/><stop offset="1" stop-color="#6f7f5a"/>
          </linearGradient>
        </defs>
        <rect x="0" y="0" width="251" height="140" fill="url(#g-tipi)" role="img" aria-label="Foto: Tipi-Zelte am Flussufer"/>
        <rect x="0" y="340" width="251" height="188" fill="url(#g-canoe2)" role="img" aria-label="Foto: Paddlerinnen im roten Kanadier"/>
        <path d="M0,25 C40,22 100,22 127,31 C100,45 45,55 54,71 C70,100 180,115 251,121 V378 C160,372 80,365 0,358 Z" fill="var(--white)" stroke="var(--orange)" stroke-width="20"/>
        <path d="M0,25 C40,22 100,22 127,31 C100,45 45,55 54,71 C70,100 180,115 251,121 V378 C160,372 80,365 0,358 Z" fill="var(--white)"/>
      </svg>
      <h2 class="title title--red" style="left:25px; top:158px; font-size:26px;">Schlauchboote</h2>
      <div class="subtitle" style="left:25px; top:191px; color:var(--orange); font-size:11px;">... Kentern ausgeschlossen!</div>
      <div class="body-copy" style="left:25px; top:210px; width:210px;">
        <p>Ab sofort bieten wir tolle Touren auf der Weser, sowie der Leine in Raftboten an. In diesen Booten finden bis zu 12 Personen Platz. Eine Tour mit unseren Tivorunden ist eine tolle Alternative um auch „alle“ mit ins Boot zu bekommen. Einfache Handhabung und bequeme Sitzposition sind garantiert.</p>
      </div>
    </section>

    <section class="panel col-3 panel--camp">
      <svg class="bg" viewBox="0 0 251 528">
        <defs>
          <linearGradient id="g-camp" x1="0" y1="0" x2="0" y2="1">
            <stop offset="0" stop-color="#6f8a6a"/><stop offset="0.5" stop-color="#d9d7cc"/><stop offset="1" stop-color="#5c8f30"/>
          </linearGradient>
          <linearGradient id="g-river" x1="0" y1="0" x2="0" y2="1">
            <stop offset="0" stop-color="#6f9a3e"/><stop offset="0.4" stop-color="#4f6f30"/><stop offset="1" stop-color="#5f7f35"/>
          </linearGradient>
          <linearGradient id="g-archery" x1="0" y1="0" x2="0" y2="1">
            <stop offset="0" stop-color="#d9e4ea"/><stop offset="0.5" stop-color="#6f9a3e"/><stop offset="1" stop-color="#8b8a7a"/>
          </linearGradient>
          <linearGradient id="g-bridge" x1="0" y1="0" x2="0" y2="1">
            <stop offset="0" stop-color="#5f8f3a"/><stop offset="0.6" stop-color="#7a6f5a"/><stop offset="1" stop-color="#5a6a5a"/>
          </linearGradient>
        </defs>
        <rect x="0" y="0" width="251" height="150" fill="url(#g-camp)" role="img" aria-label="Foto: Gruppe beim Picknick unter einem Sonnensegel am Fluss"/>
        <rect x="0" y="370" width="251" height="158" fill="url(#g-river)" role="img" aria-label="Foto: grünes Flussufer"/>
        <path d="M0,133 C80,136 180,142 251,160 V398 C170,392 80,385 0,378 Z" fill="var(--white)" stroke="var(--orange)" stroke-width="20"/>
        <path d="M0,133 C80,136 180,142 251,160 V398 C170,392 80,385 0,378 Z" fill="var(--white)"/>
        <circle cx="167" cy="184" r="56" fill="url(#g-archery)" stroke="var(--red)" stroke-width="5" role="img" aria-label="Foto: Bogenschießen auf der Wiese"/>
        <circle cx="75" cy="264" r="51" fill="url(#g-bridge)" stroke="var(--orange)" stroke-width="5" role="img" aria-label="Foto: Kanu vor einer Steinbrücke"/>
        <circle cx="167" cy="333" r="41" fill="url(#g-bridge)" stroke="var(--red)" stroke-width="5" role="img" aria-label="Foto: Paddler auf dem Fluss"/>
      </svg>
    </section>
  </div>
</div>
</body>
</html>
```